Rack Card for Charter Sail Boat business in SF Bay

We are in need of a rack card design to highlight the business to tourists and locals. 2 sided card 3.86" x 8.39" (full bleed)

We are looking for visually appleaing designs on the front and back but a little more detail on the back.

Use the info provided (text and info) on the website to include the 3 key services (Quick, 1/2 day, fullday) and aspects of the boat, location and other key info for customers (not prices). DO NOT INCLUDE ALL THIS TEXT please pick the elements you would like to fit your design and inform the customer as you would like about the business.

I can also provide photos directly from the video if you think those would fit your design. If video doesn't work on this upload you can view it at the website or facebook page (www.fb.com/tidewrenllc)

Now included a few video pictures in files for your use

Target Market(s)

Tourists and locals to san francisco east bay. 25 - 55 years old. Men and women.

Industry/Entity Type

Entertainment

Colors
0455a3
ec1f27
f3f1f8

Requirements
Must have
• Highlight services, key contact information (email, phone, website site), Visual impact
• 2-sided card - 3.86" x 8.39" (98 x 213 mm)
Nice to have
• facebook link, electric engine(green),

```html
<!DOCTYPE html>
<html lang="en">
<head>
<meta charset="utf-8">
<title>Tidewren Sail – Rack Card</title>
<link rel="stylesheet" href="https://fonts.googleapis.com/css2?family=Kaushan+Script&family=Arimo:wght@400&family=Roboto+Condensed:wght@300;400&family=Oswald:wght@500&display=swap">
<style>
:root{
  --blue:#0455a3;
  --navy:#173a7a;
  --deep:#0d2a63;
  --red:#ec1f27;
  --paper:#f3f1f8;
  --yellow:#ffe600;
  --green:#0c6b34;
  --map:#cfe2f3;
  --bg:#e9e6ee;
  --script:"Kaushan Script",cursive;
  --body:"Arimo",Arial,sans-serif;
  --cond:"Roboto Condensed",Arial Narrow,sans-serif;
  --contact:"Oswald",Arial Narrow,sans-serif;
}
*{box-sizing:border-box;margin:0;padding:0}
html,body{width:1200px;height:1200px;overflow:hidden;background:var(--bg)}
.stage{position:relative;width:1200px;height:1200px}
.card{position:absolute;top:116px;width:444px;height:966px;overflow:hidden;box-shadow:0 4px 14px rgba(0,0,0,.25)}
.card-front{left:108px;background:#fff}
.card-back{left:634px;background:var(--navy)}
.card svg.bg{position:absolute;inset:0}
.abs{position:absolute}

/* front */
.brand{position:absolute;left:250px;top:44px;display:flex;align-items:center;gap:8px}
.brand-dot{width:22px;height:22px;border-radius:50%;background:var(--blue)}
.brand-name{font-family:var(--script);font-size:38px;color:var(--blue);line-height:1}
.tagline{left:12px;top:270px;width:210px;font-family:var(--script);color:#fff;font-size:24px;line-height:33px;white-space:nowrap}
.tagline .hl{color:var(--yellow)}
.photo-circle{position:absolute;border-radius:50%;border:7px solid #fff;box-shadow:0 2px 8px rgba(0,0,0,.3)}
.feature{position:absolute;font-family:var(--body);font-size:12.6px;line-height:14.2px;color:#222}
.feature h2{font-family:var(--script);font-weight:400;font-size:36px;line-height:40px;margin-bottom:6px}
.feature .red{color:var(--red)} .feature .blue{color:var(--blue)}
.contact-line{position:absolute;display:flex;align-items:center;gap:7px;font-family:var(--contact);font-weight:500;color:#fff;font-size:15px;letter-spacing:-.3px;white-space:nowrap}
.contact-line svg{flex:none}
.card-back .contact-line{font-size:14px}

/* back */
.trip-title{left:16px;top:14px;font-family:var(--script);color:#fff;font-size:46px;line-height:1}
.trip-intro{left:16px;top:76px;width:420px;font-family:var(--body);color:#fff;font-size:12.6px;line-height:14.2px}
.service{position:absolute;border-radius:50%;border:6px solid #fff;box-shadow:0 3px 10px rgba(0,0,0,.35);display:flex;flex-direction:column;align-items:center;justify-content:center;text-align:center;padding:0 24px}
.service h3{font-family:var(--script);font-weight:400;color:var(--yellow);font-size:25px;line-height:27px;margin-bottom:6px;white-space:nowrap}
.service p{font-family:var(--cond);font-weight:300;color:#fff;font-size:13.6px;line-height:16.5px}
.service-blast{background:radial-gradient(circle at 50% 35%,#e8262c,#c4141b)}
.service-half{background:radial-gradient(circle at 50% 35%,#2444a0,#18307c)}
.service-full{background:radial-gradient(circle at 50% 35%,#147a3d,#0a5228)}
.badge{position:absolute;left:14px;top:808px;width:74px;height:74px;border-radius:50%;background:var(--deep);border:3px solid #e7b62a}
.contact-title{left:142px;top:834px;font-family:var(--script);color:#fff;font-size:44px;line-height:1}
</style>
</head>
<body>
<div class="stage">

  <!-- FRONT -->
  <section class="card card-front">
    <svg class="bg" width="444" height="966" viewBox="0 0 444 966">
      <defs>
        <linearGradient id="sunset" x1="0" y1="0" x2="0" y2="1">
          <stop offset="0" stop-color="#3d6fa8"/>
          <stop offset=".35" stop-color="#b9c9d6"/>
          <stop offset=".48" stop-color="#f4c56a"/>
          <stop offset=".6" stop-color="#6f7f90"/>
          <stop offset="1" stop-color="#2c3f57"/>
        </linearGradient>
        <linearGradient id="bandBlue" x1="0" y1="0" x2="1" y2="1">
          <stop offset="0" stop-color="#1d4f9e"/>
          <stop offset="1" stop-color="#0b3b84"/>
        </linearGradient>
      </defs>
      <rect width="444" height="360" fill="url(#sunset)" role="img" aria-label="Photo: view from the deck of the sailboat at sunset over the bay"/>
      <rect x="230" y="0" width="214" height="140" fill="#f3f5f9" opacity=".92"/>
      <path d="M0,250 Q160,220 320,290 L444,300 L444,540 Q230,440 0,525 Z" fill="var(--red)"/>
      <path d="M0,262 Q160,236 320,300 L444,312 L444,528 Q230,432 0,512 Z" fill="url(#bandBlue)"/>
      <path d="M20,522 Q120,480 230,466 L230,472 Q120,488 20,522 Z" fill="var(--red)"/>
      <path d="M0,885 Q110,845 250,882 Q360,910 444,860 L444,966 L0,966 Z" fill="var(--blue)"/>
      <path d="M300,912 Q390,895 444,835 L444,870 Q400,918 300,912 Z" fill="var(--red)"/>
      <path d="M380,640 Q420,600 444,560 L444,600 Q420,630 380,640 Z" fill="var(--red)"/>
    </svg>

    <div class="brand"><span class="brand-dot"></span><span class="brand-name">Tidewren</span></div>

    <p class="abs tagline">Enjoy an amazing<br>experience aboard<br><span class="hl">Tidewren</span> and view<br>San Francisco and<br>the rest of the bay</p>

    <div class="photo-circle" role="img" aria-label="Photo: sails and rail against a blue sky over the bay" style="left:224px;top:160px;width:220px;height:220px;background:linear-gradient(160deg,#1f67c9 0%,#5c94d8 45%,#2a4f78 75%,#1a3556 100%)"></div>
    <div class="photo-circle" role="img" aria-label="Photo: cabin interior of the sailboat" style="left:328px;top:352px;width:130px;height:130px;background:linear-gradient(150deg,#c98b4e,#f0e6d8 55%,#8a5b3a)"></div>
    <div class="photo-circle" role="img" aria-label="Photo: sunlit water with hills on the horizon" style="left:220px;top:360px;width:140px;height:140px;background:linear-gradient(180deg,#86b8ea 0%,#3f6d98 45%,#1e4f86 60%,#0f3768 100%)"></div>
    <div class="photo-circle" role="img" aria-label="Photo: the sailboat moored at the marina" style="left:186px;top:470px;width:200px;height:200px;background:linear-gradient(180deg,#7fb0e4 0%,#c9d6e2 40%,#3a8d9a 62%,#16535e 100%)"></div>

    <div class="feature" style="left:20px;top:538px;width:165px">
      <h2 class="red">Modern</h2>
      <p>Tidewren is completely electric which means no diesel smells, noise or vibration to suffer. New electrics, plumbing, toilets, and deck areas compliment the elegant lines.</p>
    </div>
    <div class="feature" style="left:20px;top:700px;width:190px">
      <h2 class="blue">Entertaining</h2>
      <p>Experience the thrill of sailing Tidewren while we explore Alcatraz and Angel Islands', The Golden Gate and Bay Bridges, the City front or the many other hidden gems.</p>
    </div>
    <div class="feature" style="left:258px;top:684px;width:180px">
      <h2 class="red">Safe</h2>
      <p>We carry aboard everything to make your time aboard safe. Life preservers and USCG bulky ones as well as modern self inflating slim comfortable life jackets. Also loaded for every trip is a complete first aid kit, AED, EPIRB, and many other safety items</p>
    </div>

    <div class="contact-line" style="left:20px;top:906px">
      <svg width="20" height="20" viewBox="0 0 20 20"><circle cx="10" cy="10" r="9" fill="none" stroke="#fff" stroke-width="1.6"/><path d="M6.5,5.5 l2,0 l.8,2.4 -1.3,1 q1,2 3,3 l1,-1.3 2.4,.8 0,2 q-5,.5 -7.9,-5.4 z" fill="#fff"/></svg>
      <span>+1 (510) 555 WREN (9736)</span>
    </div>
    <div class="contact-line" style="left:20px;top:934px">
      <svg width="20" height="16" viewBox="0 0 20 16"><rect x="1" y="1" width="18" height="14" fill="none" stroke="#fff" stroke-width="1.6"/><path d="M1,1 L10,9 L19,1" fill="none" stroke="#fff" stroke-width="1.6"/></svg>
      <span>Bookings@TidewrenSail.com</span>
    </div>
  </section>

  <!-- BACK -->
  <section class="card card-back">
    <svg class="bg" width="444" height="966" viewBox="0 0 444 966">
      <defs>
        <linearGradient id="sky" x1="0" y1="0" x2="0" y2="1">
          <stop offset="0" stop-color="#2a4f8e"/>
          <stop offset=".5" stop-color="#1f4a96"/>
          <stop offset="1" stop-color="#173a7a"/>
        </linearGradient>
        <linearGradient id="shore" x1="0" y1="0" x2="0" y2="1">
          <stop offset="0" stop-color="#1f3f78"/>
          <stop offset="1" stop-color="#173a7a"/>
        </linearGradient>
      </defs>
      <rect width="444" height="220" fill="url(#sky)" role="img" aria-label="Photo: the bay at dusk with the bridge in the distance"/>
      <path d="M0,205 Q130,160 270,182 Q370,195 444,190 L444,770 Q300,745 180,765 Q80,782 0,790 Z" fill="var(--map)" role="img" aria-label="Map of San Francisco Bay with dotted routes for each trip"/>
      <path d="M0,205 Q130,160 270,182 Q370,195 444,190 L444,202 Q370,210 270,196 Q130,176 0,220 Z" fill="var(--red)"/>
      <path d="M0,400 Q200,330 444,370" fill="none" stroke="var(--blue)" stroke-width="3"/>
      <path d="M0,580 Q220,650 444,600" fill="none" stroke="var(--blue)" stroke-width="3"/>
      <path d="M0,560 Q40,530 80,520" fill="none" stroke="var(--red)" stroke-width="3"/>
      <path d="M0,790 Q80,782 180,765 Q300,745 444,770 L444,966 L0,966 Z" fill="url(#shore)" role="img" aria-label="Photo: the city shoreline across the water at night"/>
      <path d="M240,772 Q360,740 444,712 L444,744 Q360,770 240,772 Z" fill="var(--red)"/>
      <rect x="0" y="890" width="444" height="76" fill="var(--deep)" opacity=".55"/>
    </svg>

    <h1 class="abs trip-title" style="font-weight:400">The trip</h1>
    <p class="abs trip-intro">When chartering Tidewren, the vessel is yours to direct anywhere within the time you wish to enjoy her. We do have a few old favorites that are always fun that we have listed below. These are just to provide an idea of the possible cruise as every trip takes into account your ideas and natures (tides, weather and currents) will.Our custom trips are simple to arrange and book, we simply ask for a minimum of 3 hours duration.</p>

    <div class="service service-blast" style="left:230px;top:206px;width:196px;height:196px">
      <h3>2 hour Blast</h3>
      <p>Could be a sunset sail, an early morning wake up cruise or a blast out into the bay anytime to find peace, fresh air and amazing views.</p>
    </div>
    <div class="service service-half" style="left:10px;top:390px;width:200px;height:200px">
      <h3>½ day Fun</h3>
      <p>A full morning, afternoon or evening out in the Bay seeing many of the main features and landmarks close to the Bay from the water. Actual duration 4-5 hours</p>
    </div>
    <div class="service service-full" style="left:234px;top:586px;width:196px;height:196px">
      <h3>Full Day<br>Adventure</h3>
      <p>The day includes a complete circuit of the Bay and lunch at anchor. Actual duration 7-8 hours</p>
    </div>

    <div class="badge" role="img" aria-label="Licensed captain badge"></div>
    <h2 class="abs contact-title" style="font-weight:400">Contact</h2>

    <div class="contact-line" style="left:34px;top:904px">
      <svg width="18" height="18" viewBox="0 0 20 20"><circle cx="10" cy="10" r="9" fill="none" stroke="#fff" stroke-width="1.6"/><path d="M6.5,5.5 l2,0 l.8,2.4 -1.3,1 q1,2 3,3 l1,-1.3 2.4,.8 0,2 q-5,.5 -7.9,-5.4 z" fill="#fff"/></svg>
      <span>+1 (510) 555 WREN (9736)</span>
    </div>
    <div class="contact-line" style="left:228px;top:904px">
      <svg width="18" height="14" viewBox="0 0 20 16"><rect x="1" y="1" width="18" height="14" fill="none" stroke="#fff" stroke-width="1.6"/><path d="M1,1 L10,9 L19,1" fill="none" stroke="#fff" stroke-width="1.6"/></svg>
      <span>Bookings@TidewrenSail.com</span>
    </div>
    <div class="contact-line" style="left:88px;top:936px;font-size:13px">
      <svg width="16" height="16" viewBox="0 0 16 16"><circle cx="8" cy="8" r="7" fill="none" stroke="#fff" stroke-width="1.3"/><ellipse cx="8" cy="8" rx="3" ry="7" fill="none" stroke="#fff" stroke-width="1.1"/><path d="M1,8 H15 M2.5,4.5 H13.5 M2.5,11.5 H13.5" stroke="#fff" stroke-width="1"/></svg>
      <span>www.tidewrensail.com</span>
    </div>
    <div class="contact-line" style="left:238px;top:936px;font-size:13px">
      <svg width="16" height="16" viewBox="0 0 16 16"><circle cx="8" cy="8" r="7" fill="none" stroke="#fff" stroke-width="1.3"/></svg>
      <span>/tidewrenllc</span>
    </div>
  </section>

</div>
</body>
</html>
```